Broschüre Notduschen Topseller
Zielgruppe
Ein familiengeführtes und mittelständisches Unternehmen mit unterschiedlichen Geschäftsbereichen.
K-VORTAL* ist bereits seit Mitte der 80er Jahre als Anbieter von Augenduschen und Notduschen in Deutschland bekannt und hat den Marktanteil durch die konsequente Erweiterung der Produktpalette in Verbindung mit dem höchstmöglichen Qualitätsanspruch kontinuierlich ausgebaut. Bereits im Jahre 2008 wurde die Marke K-VORTAL für professionelle Notduschsysteme und Arbeitsschutzprodukte am Markt etabliert. Seit dem 01.01.2012 firmiert K-VORTAL auch als K-VORTAL GmbH und ist heute einer der führenden Hersteller für Notduschen und Augenduschen in Europa.
Aufgabenstellung
In der word Datei ist soweit alles selbsterklärend. Zwischen den Texten ist vermerkt,
was an Bildern und Logos dazu kommt. Fehlende Daten (Logo und weitere Bilder) senden
wir dann noch, mehr konnten wir hier nicht einstellen.
Mischung aus technischer Beschreibung und Katalog
Broschüre, beidseitig bedruckt, DIN A4 Format
Wenn chic, dann zukünftig auch mehr Broschüren.

```html
<!DOCTYPE html>
<html lang="de">
<head>
<meta charset="utf-8">
<title>Hand-Augenduschen – Broschüre</title>
<link rel="stylesheet" href="https://fonts.googleapis.com/css2?family=Montserrat:wght@600;700;800&family=Roboto:wght@300;400;700&display=swap">
<style>
:root{
  --green:#4cae32;
  --green-light:#76bf43;
  --ink:#4a4a4a;
  --text:#5c5c5c;
  --yellow:#e9b800;
  --paper:#ffffff;
  --bg:#dcdcdc;
  --soft:#f0f0f0;
}
*{box-sizing:border-box;margin:0;padding:0}
html,body{width:1200px;height:833px;overflow:hidden;background:var(--bg)}
body{font-family:"Roboto",Arial,sans-serif;color:var(--text)}
.spread{position:absolute;left:40px;top:20px;width:1120px;height:792px;display:flex;box-shadow:0 10px 30px rgba(0,0,0,.18)}
.page{position:relative;width:560px;height:792px;background:var(--paper);overflow:hidden}
.page--left{border-right:1px solid #e6e6e6}

/* left page */
.kicker{position:absolute;left:48px;top:72px;font-family:"Montserrat",sans-serif;font-weight:700;font-size:15px;color:var(--green);letter-spacing:.3px}
.headline{position:absolute;left:46px;top:90px;font-family:"Montserrat",sans-serif;font-weight:800;font-size:36px;color:var(--ink);letter-spacing:.5px}
.intro{position:absolute;left:48px;top:145px;width:470px;font-size:11.5px;line-height:15px;font-weight:300}
.intro b{font-weight:700}
.hero{position:absolute;left:0;top:210px;width:560px;height:270px}
.features-title{position:absolute;left:48px;top:520px;font-family:"Montserrat",sans-serif;font-weight:700;font-size:15px;color:var(--green)}
.features{position:absolute;list-style:none;font-size:11px;line-height:14px;font-weight:300}
.features--a{left:48px;top:550px;width:215px}
.features--b{left:300px;top:450px;width:230px}
.features li{position:relative;padding-left:22px;margin-bottom:8px}
.features li b{font-weight:700;color:var(--ink)}
.features li::before{content:"";position:absolute;left:3px;top:2px;width:5px;height:9px;border:solid var(--yellow);border-width:0 2px 2px 0;transform:rotate(45deg)}
.folio{position:absolute;bottom:38px;font-family:"Montserrat",sans-serif;font-weight:700;font-size:10px;color:var(--green)}
.page--left .folio{right:48px}
.page--right .folio{left:48px}

/* right page */
.decor{position:absolute;left:0;top:0;width:560px;height:330px}
.brand{position:absolute;right:60px;top:40px;font-family:"Montserrat",sans-serif;font-weight:700;font-size:17px;color:var(--green);letter-spacing:1px}
.product-photo{position:absolute;left:90px;top:80px;width:380px;height:220px;border-radius:50%;background:radial-gradient(ellipse at 50% 50%,#2f9a7c 0%,#6a9a88 40%,rgba(240,240,240,0) 72%)}
.specs{position:absolute;left:36px;top:340px;width:488px;border-collapse:collapse;table-layout:fixed;font-size:9.5px;line-height:12px}
.specs th{background:var(--green);color:#fff;font-family:"Montserrat",sans-serif;font-weight:700;font-size:9px;text-align:left;padding:6px 5px;vertical-align:bottom;white-space:nowrap}
.specs th small{display:block;font-weight:600;font-size:7.5px}
.specs td{padding:6px 5px 8px;vertical-align:top;font-weight:300;border-bottom:1px dotted var(--green-light)}
.specs tr:last-child td{border-bottom:0}
.specs .sku{font-weight:700;color:var(--ink);white-space:nowrap}
.specs .price{font-weight:700;color:var(--ink);text-align:right;white-space:nowrap}
.specs .num{white-space:nowrap}
.rule{position:absolute;left:36px;top:510px;width:488px;height:1px;background:var(--yellow)}
.tech-title{position:absolute;left:48px;top:540px;font-family:"Montserrat",sans-serif;font-weight:700;font-size:15px;color:var(--green)}
.tech{position:absolute;left:48px;top:566px;font-size:11px;line-height:15px;display:grid;grid-template-columns:120px auto;column-gap:8px}
.tech dt{font-weight:700;color:var(--ink)}
.tech dd{font-weight:300}
.norms{position:absolute;left:310px;top:540px;width:220px;font-size:11px;line-height:14px;font-weight:300}
.norms strong{display:block;font-weight:700;color:var(--ink)}
.claims{position:absolute;left:300px;top:630px;display:flex;gap:16px;list-style:none;font-family:"Montserrat",sans-serif;font-weight:600;font-size:9.5px;color:var(--ink);letter-spacing:.4px}
.claims li::before{content:"+ ";color:var(--yellow);font-weight:800}
</style>
</head>
<body>
<main class="spread">

  <section class="page page--left">
    <p class="kicker">IM NOTFALL ZÄHLT JEDE SEKUNDE</p>
    <h1 class="headline">HAND-AUGENDUSCHEN</h1>
    <p class="intro"><b>Zwei Duschen in einer – das ist möglich durch die einzigartige Konstruktion dieser Duschen:</b> die Hand-Augenduschen können als fest installierte Augendusche in der Halterung betrieben werden, oder aber aus der Halterung entnommen werden, um als Handbrause am Boden liegende Verletzte zu versorgen. <b>Wählen Sie aus einer Vielzahl von Modellen mit einem oder zwei Brauseköpfen.</b></p>

    <svg class="hero" viewBox="0 0 560 270">
      <defs>
        <linearGradient id="heroTone" x1="0" y1="0" x2="1" y2="0">
          <stop offset="0" stop-color="#f1d6cc"/>
          <stop offset=".45" stop-color="#e6ebe8"/>
          <stop offset="1" stop-color="#c9d6d2"/>
        </linearGradient>
        <radialGradient id="insetTone" cx=".5" cy=".5" r=".6">
          <stop offset="0" stop-color="#5c8c7c"/>
          <stop offset="1" stop-color="#e8ecea"/>
        </radialGradient>
      </defs>
      <path d="M0 110 C160 40 360 10 560 0 L560 150 C380 150 180 190 0 250 Z" fill="url(#heroTone)" role="img" aria-label="Foto: Person spült sich die Augen an einer wandmontierten Hand-Augendusche"/>
      <path d="M0 100 C160 30 360 0 560 -10 L560 6 C360 16 160 46 0 118 Z" fill="var(--green)"/>
      <path d="M0 250 C180 190 380 150 560 150 L560 175 C380 172 200 210 40 270 L0 270 Z" fill="var(--green-light)"/>
      <circle cx="150" cy="200" r="64" fill="#fff"/>
      <circle cx="150" cy="200" r="60" fill="url(#insetTone)" role="img" aria-label="Detailfoto: Hand-Augendusche in der Wandhalterung"/>
    </svg>

    <h2 class="features-title">Umfangreiche Features:</h2>
    <ul class="features features--a">
      <li><b>K-VORTAL Hochleistungsbrauseköpfe</b> für einen begrenzten, gleichmäßigen und weichen Wasserstrahl – optimiert für das Ausspülen von Chemikalien im Auge</li>
      <li><b>Integrierter automatischer Mengenregulator</b> für die richtige Strahlhöhe unabhängig vom Wasserdruck</li>
      <li><b>Integrierter Rückflussverhinderer</b> zum Schutz des Trinkwassernetzes</li>
    </ul>
    <ul class="features features--b">
      <li><b>Gummimuffen</b> um den Brausekopf schützen den Hilfesuchenden vor Stoßverletzungen</li>
      <li><b>Staubabdeckkappen</b> öffnen bei Betätigung der Augendusche durch den Wasserdruck selbstständig</li>
      <li><b>Große Bohrungen</b> in den Brauseköpfen verhindern stehendes Wasser und somit Verkalkung</li>
    </ul>
    <span class="folio">02</span>
  </section>

  <section class="page page--right">
    <svg class="decor" viewBox="0 0 560 330" aria-hidden="true">
      <circle cx="300" cy="160" r="230" fill="var(--soft)"/>
      <circle cx="470" cy="40" r="200" fill="#fff"/>
    </svg>
    <div class="brand">K-VORTAL</div>
    <div class="product-photo" role="img" aria-label="Produktfotos: drei Hand-Augenduschen in Grün und Grau mit Halterungen"></div>

    <table class="specs">
      <colgroup>
        <col style="width:68px"><col style="width:170px"><col style="width:102px"><col style="width:50px"><col style="width:28px"><col style="width:70px">
      </colgroup>
      <thead>
        <tr>
          <th>Artikel-Nr.</th>
          <th>Ausführung</th>
          <th>Versandeinheit<small>Abmessungen: L x B x H</small></th>
          <th>Gewicht</th>
          <th>PG</th>
          <th style="text-align:right">Preis<small>pro Stück</small></th>
        </tr>
      </thead>
      <tbody>
        <tr><td class="sku">KV 412 730</td><td>StandardLine Sicherheits-Augendusche mit zwei Brauseköpfen 45°, für Wandmontage</td><td class="num">380 x 290 x 100 mm</td><td class="num">1,42 kg</td><td>86</td><td class="price">255,00 €</td></tr>
        <tr><td class="sku">KV 516 240</td><td>StandardLine Sicherheits-Augendusche mit Auffangbecken, für Wandmontage</td><td class="num">400 x 300 x 215 mm</td><td class="num">3,81 kg</td><td>86</td><td class="price">450,00 €</td></tr>
        <tr><td class="sku">KV 938 110</td><td>ExklusivLine Augen-/Gesichtsdusche mit Auffangbecken und Abdeckung, für Wandmontage</td><td class="num">375 x 290 x 370 mm</td><td class="num">3,90 kg</td><td>86</td><td class="price">625,00 €</td></tr>
      </tbody>
    </table>
    <div class="rule"></div>

    <h2 class="tech-title">Technische Daten:</h2>
    <dl class="tech">
      <dt>Wasseranschluss:</dt><dd>1/2-Zoll-IG</dd>
      <dt>Schlauchlänge:</dt><dd>1500 mm</dd>
      <dt>Volumenstrom:</dt><dd>7 l/min pro Brausekopf</dd>
    </dl>
    <p class="norms"><strong>Normen / Zulassungen:</strong>DIN EN 15154-2:2006, ANSI Z358.1-2014<br>WQPA, QZ-2281KV0415</p>
    <ul class="claims"><li>SICHER</li><li>LEISTUNGSSTARK</li><li>EFFIZIENT</li></ul>
    <span class="folio">03</span>
  </section>

</main>
</body>
</html>
```